Landing Page Design for Adult Dating Age Verification (18+)

The objective of this task is to design a visually appealing pre-landing page for the adult dating site "Plumvelle (site: https://plumvelle.example/)" with an age verification mechanism. The pre-landing page will feature two buttons that redirect visitors to the main offer. The design should also include a footer block that includes links to the terms of use, privacy policy, and contact us pages.

Design Requirements:
Develop an age verification section prominently displayed on the pre-landing page.
Design the section to include two buttons labeled "Yes" and "No" for visitors to confirm their age.
Ensure the section is visually appealing and clearly communicates the purpose of age verification.

Visual Appeal:
Create a visually appealing design that aligns with the branding and theme of the "Plumvelle" adult dating site.
Use suitable color schemes, typography, and graphics to enhance the overall visual appeal of the pre-landing page.

Layout and Navigation:
Design an engaging and intuitive layout that encourages visitors to interact with the page and proceed to the main offer.
Ensure clear and visible navigation elements that direct visitors to the main offer or provide additional information.

Responsive Design:
Develop a responsive design that provides a seamless user experience across various devices, including desktop and mobile.
Ensure the design elements and layout adapt well to different screen sizes and resolutions.

File Formats and Assets:
Deliver the final design in PSD, AI, or Sketch format, ensuring that the files are well-organized and layered.
Include any necessary images or assets used in the design, ensuring they are of high quality and optimized for web use.

```html
<!DOCTYPE html>
<html lang="en">
<head>
<meta charset="utf-8">
<title>Plumvelle — Find Your Match</title>
<link href="https://fonts.googleapis.com/css2?family=Fredoka:wght@400;500;600&family=Andika:wght@400;700&display=swap" rel="stylesheet">
<style>
  :root {
    --plum: #b07cc0;
    --plum-button: #b485c3;
    --plum-soft: #d9bfe0;
    --ink: #1c1a22;
    --logo-ink: #2a2631;
    --room-light: #fbfbfa;
    --room-mid: #eeeeec;
    --room-shade: #dcdcda;
    --white: #ffffff;
  }
  * { box-sizing: border-box; margin: 0; padding: 0; }
  html, body { width: 1200px; height: 547px; overflow: hidden; background: var(--room-light); }
  .landing {
    position: relative;
    width: 1200px;
    height: 547px;
    overflow: hidden;
    font-family: "Andika", sans-serif;
    color: var(--ink);
  }
  .room-scene {
    position: absolute;
    inset: 0;
    background:
      linear-gradient(90deg, rgba(255,255,255,0.95) 0%, rgba(255,255,255,0.85) 40%, rgba(255,255,255,0) 62%),
      linear-gradient(180deg, var(--room-light) 0%, var(--room-mid) 55%, var(--room-shade) 100%);
  }
  .couple-scene {
    position: absolute;
    left: 705px;
    top: 20px;
    width: 305px;
    height: 527px;
    border-radius: 140px 140px 0 0;
    background: linear-gradient(180deg, #ead7c4 0%, #f4eee8 30%, #f6f4f1 55%, #6f8fb8 75%, #3f5f8f 100%);
    opacity: 0.85;
  }
  .brand {
    position: absolute;
    left: 116px;
    top: 92px;
    display: flex;
    align-items: center;
    gap: 14px;
  }
  .brand-dot {
    width: 64px;
    height: 64px;
    border-radius: 50%;
    background: var(--plum-soft);
  }
  .brand-name {
    font-family: "Fredoka", sans-serif;
    font-weight: 500;
    font-size: 38px;
    color: var(--logo-ink);
    letter-spacing: 0.5px;
  }
  .hero {
    position: absolute;
    left: 116px;
    top: 222px;
  }
  .hero-title {
    font-family: "Fredoka", sans-serif;
    font-weight: 500;
    font-size: 48px;
    line-height: 1.1;
    color: var(--plum);
  }
  .hero-intro {
    margin-top: 12px;
    font-size: 16.5px;
    font-weight: 700;
    line-height: 28px;
  }
  .age-check { margin-top: 18px; }
  .age-question { font-size: 16px; }
  .age-actions {
    margin-top: 8px;
    display: flex;
    gap: 10px;
  }
  .age-button {
    width: 54px;
    height: 41px;
    display: flex;
    align-items: center;
    justify-content: center;
    background: var(--plum-button);
    color: var(--white);
    font-family: "Andika", sans-serif;
    font-size: 18px;
    text-decoration: none;
  }
  .remember {
    margin-top: 14px;
    display: flex;
    align-items: center;
    gap: 7px;
    font-size: 13px;
  }
  .remember-box {
    width: 13px;
    height: 13px;
    border: 1px solid #8d7f93;
    background: #f4eef5;
  }
</style>
</head>
<body>
  <main class="landing">
    <div class="room-scene" role="img" aria-label="Bright white room with brick walls, tall windows and radiators"></div>
    <div class="couple-scene" role="img" aria-label="Young couple in white shirts and jeans embracing forehead to forehead"></div>

    <a class="brand" href="https://plumvelle.example/">
      <span class="brand-dot"></span>
      <span class="brand-name">Plumvelle</span>
    </a>

    <section class="hero">
      <h1 class="hero-title">Find Your Match</h1>
      <p class="hero-intro">Welcome to Our Dating Site.The Place Where<br>Your can Find What Your Heart Desires!</p>
      <div class="age-check">
        <p class="age-question">Are You Over 18 years of Age?</p>
        <div class="age-actions">
          <a class="age-button" href="https://plumvelle.example/">Yes</a>
          <a class="age-button" href="https://plumvelle.example/">No</a>
        </div>
        <label class="remember"><span class="remember-box"></span>Remember Me</label>
      </div>
    </section>
  </main>
</body>
</html>
```